Brightmoor Advisory

Looking for modern business cards.
Clean contemporary design.
Similar to this.
https://www.quorvexsearch.example/imgview?src=https%3A%2F%2Fimg.pellumcards.example%2Fprofessional_elegant_modern_black_plain_metal_business_card-a7c21e90b4d3f5e6a8b9c0d1e2f3a4b5_540.jpg&ref=https%3A%2F%2Fwww.pellumcards.example%2Fprofessional_elegant_modern_black_plain_metal_business_card-518273640192837465&id=7kQ2mZ9x-PL4TW&w=540&h=540&q=modern%20business%20cards

But I'd like the blue to look metallic.

```html
<!DOCTYPE html>
<html lang="en">
<head>
<meta charset="utf-8">
<title>Brightmoor Advisory – Business Cards</title>
<link href="https://fonts.googleapis.com/css2?family=Roboto:wght@300;400;700&display=swap" rel="stylesheet">
<style>
  :root {
    --backdrop: #2b2b2b;
    --metal-light: #5fabc6;
    --metal-mid: #4593b1;
    --metal-dark: #3a84a2;
    --ink: #ffffff;
    --ink-soft: #d4eef7;
    --rule: #bfe6f2;
  }
  * { box-sizing: border-box; margin: 0; padding: 0; }
  html, body {
    width: 1200px; height: 900px; overflow: hidden;
    background: var(--backdrop);
    font-family: "Roboto", Arial, sans-serif;
  }
  .stage { position: relative; width: 1200px; height: 900px; }

  .card {
    position: absolute;
    width: 620px; height: 354px;
    border-radius: 22px;
    overflow: hidden;
    color: var(--ink);
    background:
      repeating-linear-gradient(180deg, rgba(255,255,255,.05) 0 1px, rgba(0,0,0,0) 1px 3px, rgba(0,0,0,.04) 3px 4px),
      linear-gradient(115deg, rgba(255,255,255,0) 20%, rgba(255,255,255,.16) 42%, rgba(255,255,255,0) 60%),
      linear-gradient(160deg, var(--metal-light) 0%, var(--metal-mid) 45%, var(--metal-dark) 100%);
    box-shadow: 0 14px 30px rgba(0,0,0,.45);
  }
  .card--front { left: 60px; top: 90px; }
  .card--back  { left: 520px; top: 456px; }

  .wordmark {
    display: flex; align-items: center; gap: 12px;
    font-weight: 700; color: var(--ink); letter-spacing: .5px;
  }
  .wordmark__dot {
    width: 22px; height: 22px; border-radius: 50%; background: var(--ink); flex: none;
  }
  .card--front .wordmark {
    position: absolute; left: 0; right: 0; top: 150px;
    justify-content: center; font-size: 44px;
  }
  .card--back .wordmark {
    position: absolute; left: 40px; top: 48px; font-size: 30px;
  }
  .card--back .wordmark__dot { width: 16px; height: 16px; }

  .divider {
    position: absolute; left: 40px; right: 40px; top: 112px;
    height: 2px; background: var(--rule);
  }
  .address {
    position: absolute; right: 40px; top: 126px;
    text-align: right; font-weight: 300; font-size: 15px; line-height: 1.35;
    color: var(--ink-soft);
  }
  .person { position: absolute; left: 40px; top: 166px; width: 220px; }
  .person__name { font-weight: 700; font-size: 20px; letter-spacing: .3px; }
  .person__role { font-weight: 300; font-size: 14px; color: var(--ink-soft); margin-top: 1px; }
  .person__rule { height: 2px; background: var(--rule); margin-top: 8px; }

  .contacts { position: absolute; left: 40px; top: 236px; list-style: none; }
  .contacts li {
    display: flex; align-items: center; gap: 12px;
    font-weight: 300; font-size: 16px; line-height: 26px; color: var(--ink);
  }
  .contacts svg { width: 16px; height: 16px; fill: var(--ink); flex: none; }
</style>
</head>
<body>
<main class="stage">

  <section class="card card--front" aria-label="Card front">
    <div class="wordmark"><span class="wordmark__dot"></span>Brightmoor Advisory</div>
  </section>

  <section class="card card--back" aria-label="Card back">
    <div class="wordmark"><span class="wordmark__dot"></span>Brightmoor Advisory</div>
    <div class="divider"></div>
    <p class="address">12345 Your Address #111<br>United States 12345</p>

    <div class="person">
      <p class="person__name">JOHN DOE</p>
      <p class="person__role">owner</p>
      <div class="person__rule"></div>
    </div>

    <ul class="contacts">
      <li>
        <svg viewBox="0 0 24 24" aria-hidden="true"><path d="M6.6 10.8a15.1 15.1 0 0 0 6.6 6.6l2.2-2.2c.3-.3.7-.4 1-.2 1.1.4 2.3.6 3.6.6.6 0 1 .4 1 1V20c0 .6-.4 1-1 1A17 17 0 0 1 3 4c0-.6.4-1 1-1h3.5c.6 0 1 .4 1 1 0 1.3.2 2.5.6 3.6.1.3 0 .7-.2 1z"/></svg>
        123-456-1234
      </li>
      <li>
        <svg viewBox="0 0 24 24" aria-hidden="true"><path d="M3 8c0-2 4-4 9-4s9 2 9 4v2h-5V8.5c-1-.4-2.4-.6-4-.6s-3 .2-4 .6V10H3zM6 11h12l2 9H4zm6 2.5a2.5 2.5 0 1 0 0 5 2.5 2.5 0 0 0 0-5z"/></svg>
        123-111-2222
      </li>
      <li>
        <svg viewBox="0 0 24 24" aria-hidden="true"><path d="M2 5h20v14H2zm2 2v.5l8 5.5 8-5.5V7zm0 2.9V17h16V9.9l-8 5.5z"/></svg>
        yourmail@email.com
      </li>
      <li>
        <svg viewBox="0 0 24 24" aria-hidden="true"><path d="M12 2a10 10 0 1 0 0 20 10 10 0 0 0 0-20zm6.9 6h-3a15 15 0 0 0-1.3-3.9A8 8 0 0 1 18.9 8zM12 4c.8 1.2 1.5 2.5 1.9 4h-3.8c.4-1.5 1.1-2.8 1.9-4zM4.3 14a8 8 0 0 1 0-4h3.4a16 16 0 0 0 0 4zm.8 2h3a15 15 0 0 0 1.3 3.9A8 8 0 0 1 5.1 16zm3-8h-3a8 8 0 0 1 4.3-3.9C8.8 5.3 8.4 6.6 8.1 8zM12 20c-.8-1.2-1.5-2.5-1.9-4h3.8c-.4 1.5-1.1 2.8-1.9 4zm2.3-6H9.7a14 14 0 0 1 0-4h4.6a14 14 0 0 1 0 4zm.3 5.9c.6-1.2 1-2.5 1.3-3.9h3a8 8 0 0 1-4.3 3.9zm1.7-5.9a16 16 0 0 0 0-4h3.4a8 8 0 0 1 0 4z"/></svg>
        www.yourweb.com
      </li>
    </ul>
  </section>

</main>
</body>
</html>
```